Website for Apartment Rental in Prague

I would like to create designs of my website focused on Vltava Residences rentals in Prague, Czech Republic. I created initial mock-ups, They are all attached. I need to design homepage and subpage. The mock-ups were created by combining elements from different websites that I liked but I need you to create a design that is unique and original. The attached files a only a guidance for the structure of the website but not for the design. Try to be creative.

Industry/Entity Type

Apartment

```html
<!DOCTYPE html>
<html lang="en">
<head>
<meta charset="utf-8">
<title>Vltava Residences – Luxury Apartment Rentals in Prague</title>
<link rel="stylesheet" href="https://fonts.googleapis.com/css2?family=Cormorant+Garamond:wght@500;600;700&family=Manrope:wght@400;500;600;700&display=swap">
<style>
:root{
  --navy:#1c2838;
  --navy-deep:#131c28;
  --brass:#b8894a;
  --brass-dark:#9c7238;
  --cream:#f6f1e9;
  --ink:#1f2a36;
  --text:#5d6570;
  --muted:#98a0a8;
  --line:#e3ddd3;
  --sage:#4f8a6b;
  --sage-dark:#42775b;
  --white:#fff;
  --footer-text:#b9c1cb;
}
*{box-sizing:border-box;margin:0;padding:0}
html,body{width:1200px;height:3025px;overflow:hidden}
body{position:relative;background:var(--white);font-family:'Manrope',sans-serif;color:var(--text);font-size:13px}
.abs{position:absolute}
.display{font-family:'Cormorant Garamond',serif}

/* top bar */
.topbar{top:0;left:0;width:1200px;height:40px;background:var(--navy-deep);color:var(--footer-text);font-size:12px;display:flex;align-items:center;justify-content:space-between;padding:0 88px}
.topbar-group{display:flex;align-items:center;gap:22px}
.topbar-group span{display:flex;align-items:center;gap:8px}
.lang-dot{width:10px;height:10px;border-radius:50%;background:var(--brass)}
.topbar .lang{color:var(--white);font-weight:600;letter-spacing:.6px}
.topbar .sep{width:1px;height:14px;background:#33404f}

/* header */
.header{top:40px;left:0;width:1200px;height:88px;border-bottom:1px solid var(--line);display:flex;align-items:center;justify-content:space-between;padding:0 88px}
.brand{display:flex;align-items:center;gap:10px;font-family:'Cormorant Garamond',serif;font-weight:700;font-size:26px;color:var(--navy);letter-spacing:.4px}
.brand i{width:12px;height:12px;border-radius:50%;background:var(--brass)}
.nav{display:flex;align-items:center;gap:30px}
.nav a{font-size:11.5px;font-weight:600;color:var(--ink);text-decoration:none;letter-spacing:1px}
.nav a.current{color:var(--brass)}

/* hero */
.hero{top:128px;left:0;width:1200px;height:572px;background:linear-gradient(180deg,#c9cdd2 0%,#a9adb1 34%,#6c665a 58%,#3f7fa6 78%,#5f665f 100%)}
.hero-shade{top:128px;left:0;width:1200px;height:572px;background:linear-gradient(90deg,rgba(19,28,40,.72) 0%,rgba(19,28,40,.35) 55%,rgba(19,28,40,0) 100%)}
.hero-copy{top:250px;left:88px;width:620px;color:var(--white)}
.hero-kicker{display:flex;align-items:center;gap:14px;font-size:13px;font-weight:600;letter-spacing:3px;color:#e9d3b2}
.hero-kicker b{width:40px;height:1px;background:var(--brass)}
.hero-title{margin-top:18px;font-family:'Cormorant Garamond',serif;font-size:64px;font-weight:600;line-height:1.02}
.hero-btn{margin-top:30px;display:inline-block;padding:0 28px;height:46px;line-height:46px;border:1px solid var(--white);color:var(--white);font-size:11px;font-weight:700;letter-spacing:1.6px}
.hero-arrow{top:392px;width:40px;height:40px;border:1px solid rgba(255,255,255,.7);display:flex;align-items:center;justify-content:center}
.scroll-cue{top:584px;left:88px;display:flex;align-items:center;gap:12px;color:var(--white);font-size:10px;letter-spacing:2px}

/* booking */
.booking{top:660px;left:88px;width:1024px;height:300px;background:var(--white);border-top:3px solid var(--brass);box-shadow:0 14px 40px rgba(19,28,40,.14);padding:34px 34px 0}
.booking h2{font-family:'Cormorant Garamond',serif;font-size:30px;font-weight:600;color:var(--navy);text-align:center;line-height:36px}
.row{display:flex;gap:14px;margin-top:28px;align-items:flex-end}
.row + .row{margin-top:20px}
.cell{flex:1;min-width:0}
.label{display:block;font-size:10px;font-weight:700;color:var(--ink);letter-spacing:1.2px;margin-bottom:8px;white-space:nowrap}
.field{position:relative;height:44px;border:1px solid var(--line);background:var(--cream);font-size:11.5px;color:#8a8f96;padding:0 16px;line-height:42px;white-space:nowrap;overflow:hidden}
.field.select::after{content:"";position:absolute;right:16px;top:16px;width:6px;height:6px;border-right:1.5px solid var(--brass);border-bottom:1.5px solid var(--brass);transform:rotate(45deg)}
.or{flex:none;width:26px;height:44px;line-height:44px;text-align:center;font-size:11px;font-weight:700;color:var(--brass)}
.btn-brass{background:var(--brass);color:var(--white);font-size:11px;font-weight:700;letter-spacing:1.4px;text-align:center}

/* about */
.about{top:1040px;left:180px;width:840px;text-align:center}
.eyebrow{font-size:11px;font-weight:700;letter-spacing:3px;color:var(--brass)}
.section-title{font-family:'Cormorant Garamond',serif;font-size:38px;font-weight:600;color:var(--navy);line-height:44px}
.about .eyebrow{margin-bottom:12px}
.ornament{width:60px;height:1px;background:var(--brass);margin:20px auto 22px}
.about p{font-size:13px;line-height:25px;color:var(--text)}
.about .btn-brass{display:inline-block;margin-top:30px;height:46px;line-height:46px;padding:0 30px}

/* apartments */
.apartments{top:1420px;left:0;width:1200px;height:705px;background:var(--cream)}
.apartments-head{top:1500px;left:88px;width:1024px;display:flex;justify-content:space-between;align-items:flex-end}
.apartments-head .eyebrow{margin-bottom:8px}
.pager{display:flex;gap:8px}
.pager div{width:40px;height:40px;display:flex;align-items:center;justify-content:center;border:1px solid var(--navy)}
.pager div.on{background:var(--navy)}
.cards{top:1610px;left:88px;width:1024px;display:flex;gap:20px}
.card{width:328px;height:420px;background:var(--white);position:relative}
.card .photo{height:200px}
.card .tag{position:absolute;top:16px;left:16px;background:var(--white);color:var(--navy);font-size:10px;font-weight:700;letter-spacing:1.2px;padding:6px 10px}
.stats{display:flex;border-bottom:1px solid var(--line);margin:0 24px;padding:14px 0}
.stat{flex:1;font-size:10.5px;color:var(--muted);line-height:15px}
.stat svg{display:block;margin-bottom:5px}
.stat b{color:var(--ink);font-weight:700}
.card h3{margin:18px 24px 0;font-family:'Cormorant Garamond',serif;font-size:22px;font-weight:600;color:var(--navy);line-height:26px}
.card p{margin:6px 24px 0;font-size:11.5px;color:var(--text);white-space:nowrap}
.actions{position:absolute;left:24px;bottom:24px;display:flex;align-items:center;gap:20px;font-size:10.5px;font-weight:700;letter-spacing:1.2px}
.btn-outline{width:92px;height:36px;border:1px solid var(--navy);color:var(--navy);text-align:center;line-height:34px}
.btn-fill{width:92px;height:36px;background:var(--navy);color:var(--white);text-align:center;line-height:36px}
.book{color:var(--muted)}
.book.active{color:var(--brass)}

/* testimonial */
.portrait-frame{top:2230px;left:88px;width:230px;height:230px;border:1px solid var(--brass)}
.portrait{top:2250px;left:108px;width:230px;height:230px;background:linear-gradient(160deg,#c9d3da,#5b7790 60%,#2f4458)}
.quote-mark{top:2196px;left:300px;font-family:'Cormorant Garamond',serif;font-size:120px;line-height:1;color:var(--brass);font-weight:700}
.testimonial{top:2226px;left:400px;width:712px}
.testimonial .eyebrow{margin-bottom:8px}
.testimonial .pager{position:absolute;right:0;top:10px}
.testimonial p{margin-top:20px;font-family:'Cormorant Garamond',serif;font-size:21px;font-style:normal;line-height:32px;color:var(--ink)}
.author{margin-top:24px;display:flex;align-items:center;gap:18px}
.author i{width:46px;height:1px;background:var(--brass)}
.author strong{display:block;font-size:15px;font-weight:700;color:var(--navy)}
.author span{display:block;font-size:12px;color:var(--muted);margin-top:2px}
.msg-btn{top:2556px;left:892px;width:220px;height:44px;background:var(--sage);color:var(--white);font-size:10.5px;font-weight:700;letter-spacing:1.2px;display:flex;align-items:center;gap:14px}
.msg-btn .ico{width:48px;height:44px;background:var(--sage-dark);display:flex;align-items:center;justify-content:center}

/* footer */
.footer{top:2600px;left:0;width:1200px;height:425px;background:var(--navy-deep);color:var(--footer-text)}
.footer-cols{position:absolute;top:80px;left:88px;width:1024px;display:flex}
.col{padding-right:30px;margin-right:30px;border-right:1px solid #2a3646;min-height:200px}
.col:last-child{border-right:0;margin-right:0;padding-right:0}
.footer h4{font-family:'Cormorant Garamond',serif;font-weight:600;font-size:21px;color:var(--white);margin-bottom:22px;line-height:24px}
.footer ul{list-style:none;font-size:12px}
.footer li{display:flex;align-items:flex-start;gap:10px;line-height:18px;margin-bottom:14px}
.dot{width:8px;height:8px;border-radius:50%;background:var(--brass);margin-top:5px;flex:none}
.news-text{font-size:12px;line-height:20px}
.news-input{position:relative;margin-top:20px;height:44px;background:var(--white);font-size:11.5px;color:#8a8f96;line-height:44px;padding-left:36px}
.copyright{position:absolute;bottom:0;left:88px;width:1024px;height:56px;border-top:1px solid #2a3646;display:flex;align-items:center;justify-content:center;font-size:11.5px}
.to-top{top:2950px;left:1136px;width:38px;height:38px;border-radius:50%;background:var(--brass);display:flex;align-items:center;justify-content:center}
</style>
</head>
<body>

<!-- top bar -->
<div class="abs topbar">
  <div class="topbar-group">
    <span class="lang"><i class="lang-dot"></i>ENGLISH ▾</span>
    <i class="sep"></i><span>Sign In</span>
    <i class="sep"></i><span>Register</span>
    <i class="sep"></i><span>Cart</span>
  </div>
  <div class="topbar-group">
    <span><svg width="12" height="10" viewBox="0 0 12 10"><rect width="12" height="10" fill="#b8894a"/><path d="M0 0l6 5 6-5" stroke="#131c28" fill="none"/></svg>stay@vltavaresidences.cz</span>
    <i class="sep"></i>
    <span><svg width="12" height="12" viewBox="0 0 24 24"><path fill="#b8894a" d="M6.6 10.8a15 15 0 006.6 6.6l2.2-2.2a1 1 0 011-.25 11.4 11.4 0 003.6.6 1 1 0 011 1V20a1 1 0 01-1 1A17 17 0 013 4a1 1 0 011-1h3.5a1 1 0 011 1c0 1.25.2 2.45.6 3.6a1 1 0 01-.25 1z"/></svg>+420 221 480 390</span>
  </div>
</div>

<!-- header -->
<header class="abs header">
  <div class="brand"><i></i>Vltava Residences</div>
  <nav class="nav">
    <a class="current">APARTMENTS</a>
    <a>LOCATION</a>
    <a>SERVICES</a>
    <a>GALLERY</a>
    <a>NEWS</a>
    <a>EXCLUSIVE &amp; TOURS</a>
    <a>CONTACT US</a>
    <svg width="18" height="18" viewBox="0 0 20 20"><circle cx="8" cy="8" r="6.5" stroke="#1f2a36" stroke-width="2" fill="none"/><path d="M13 13l6 6" stroke="#1f2a36" stroke-width="2"/></svg>
  </nav>
</header>

<!-- hero -->
<section class="abs hero" role="img" aria-label="Modern luxury villa with glass walls beside a blue swimming pool at dusk"></section>
<div class="abs hero-shade"></div>
<div class="abs hero-copy">
  <div class="hero-kicker"><b></b>FIND YOUR DREAM APARTMENT</div>
  <h1 class="hero-title">Luxury Apartment Rentals</h1>
  <div class="hero-btn">VIEW MORE DETAILS</div>
</div>
<div class="abs hero-arrow" style="left:1062px"><svg width="8" height="12"><path d="M7 1L2 6l5 5" stroke="#fff" stroke-width="1.6" fill="none"/></svg></div>
<div class="abs hero-arrow" style="left:1110px"><svg width="8" height="12"><path d="M1 1l5 5-5 5" stroke="#fff" stroke-width="1.6" fill="none"/></svg></div>
<div class="abs scroll-cue"><svg width="20" height="30" viewBox="0 0 20 30"><rect x="1" y="1" width="18" height="28" rx="9" stroke="#fff" stroke-width="1.6" fill="none"/><rect x="9" y="7" width="2" height="6" fill="#fff"/></svg></div>

<!-- booking -->
<form class="abs booking">
  <h2>Official site - Best Price Guaranteed</h2>
  <div class="row">
    <div class="cell"><span class="label">CHECK IN DATE</span><div class="field">11-17-2017</div></div>
    <div class="cell"><span class="label">CHECK IN DATE</span><div class="field">11-18-2017</div></div>
    <div class="cell"><span class="label">ADULTS</span><div class="field select">02</div></div>
    <div class="cell"><span class="label">CHILDERN</span><div class="field select">00</div></div>
    <div class="cell"><span class="label">INFANTS</span><div class="field select">00</div></div>
  </div>
  <div class="row">
    <div class="cell" style="flex:2"><span class="label">PROMOTIONAL CODE</span><div class="field">000-000-123-456</div></div>
    <div class="or">OR</div>
    <div class="cell" style="flex:2"><span class="label">SELECT RENTAL</span><div class="field select">Select Rental Unit</div></div>
    <div class="btn-brass" style="flex:none;width:196px;height:44px;line-height:44px">CHECK AVAILABILITY</div>
  </div>
</form>

<!-- about -->
<section class="abs about">
  <div class="eyebrow">SHORT COMPANY INTRODUCTION</div>
  <h2 class="section-title">A different vision of travelling</h2>
  <div class="ornament"></div>
  <p>Proin gravida nibh vel velit auctor aliquet aenean sollicitudin, lorem quis bibendum auctor, nisi elit consequat ipsum, nec sagittis sem nibh id elit duis sed odio sit amet nibh vulputate cursus a sit amet mauris. Morbi accumsan ipsum velit nam nec tellus a odio tincidunt auctor a ornare odio sed non mauris vitae erat consequat auctor eu in elit.</p>
  <div class="btn-brass">LEARN MORE ABOUT US</div>
</section>

<!-- apartments -->
<section class="abs apartments"></section>
<div class="abs apartments-head">
  <div>
    <h2 class="section-title">Interior design apartments</h2>
  </div>
  <div class="pager">
    <div><svg width="8" height="12"><path d="M6 1L2 6l4 5" stroke="#1c2838" stroke-width="1.5" fill="none"/></svg></div>
    <div class="on"><svg width="8" height="12"><path d="M2 1l4 5-4 5" stroke="#fff" stroke-width="1.5" fill="none"/></svg></div>
  </div>
</div>

<div class="abs cards">
  <article class="card">
    <div class="photo" role="img" aria-label="Open plan white kitchen with dining area and wooden floor" style="background:linear-gradient(160deg,#e9e9e6,#b9b3aa 60%,#6e5e4e)"></div>
    <div class="stats">
      <div class="stat"><svg width="22" height="20"><rect x="1" y="1" width="18" height="18" fill="none" stroke="#b8894a" stroke-width="1.4"/><path d="M1 10h9v9" fill="none" stroke="#b8894a" stroke-width="1.4"/></svg>SQFT<br><b>2,016</b></div>
      <div class="stat"><svg width="26" height="20"><path d="M2 18V5M2 12h22v6M5 12V8h8v4" fill="none" stroke="#b8894a" stroke-width="1.4"/></svg>Bedrooms<br><b>3</b></div>
      <div class="stat"><svg width="26" height="20"><path d="M3 10h20c0 5-4 8-10 8S3 15 3 10zM6 10V3h4" fill="none" stroke="#b8894a" stroke-width="1.4"/></svg>Bathrooms<br><b>2</b></div>
      <div class="stat"><svg width="26" height="20"><path d="M2 19V7l11-5 11 5v12M6 19v-8h14v8M6 14h14" fill="none" stroke="#b8894a" stroke-width="1.4"/></svg>Garages<br><b>2</b></div>
    </div>
    <h3>New modern apartment</h3>
    <p>Proin gravida nibh vel velit auctor aliquet aenean</p>
    <div class="actions"><div class="btn-outline">DETAILS</div><span class="book">BOOK NOW</span></div>
  </article>

  <article class="card">
    <div class="photo" role="img" aria-label="Bright attic living room with sofa and arched window" style="background:linear-gradient(160deg,#d8c9b2,#a98a6c 55%,#6b4d34)"></div>
    <div class="stats">
      <div class="stat"><svg width="22" height="20"><rect x="1" y="1" width="18" height="18" fill="none" stroke="#b8894a" stroke-width="1.4"/><path d="M1 10h9v9" fill="none" stroke="#b8894a" stroke-width="1.4"/></svg>SQFT<br><b>2,016</b></div>
      <div class="stat"><svg width="26" height="20"><path d="M2 18V5M2 12h22v6M5 12V8h8v4" fill="none" stroke="#b8894a" stroke-width="1.4"/></svg>Bedrooms<br><b>3</b></div>
      <div class="stat"><svg width="26" height="20"><path d="M3 10h20c0 5-4 8-10 8S3 15 3 10zM6 10V3h4" fill="none" stroke="#b8894a" stroke-width="1.4"/></svg>Bathrooms<br><b>2</b></div>
      <div class="stat"><svg width="26" height="20"><path d="M2 19V7l11-5 11 5v12M6 19v-8h14v8M6 14h14" fill="none" stroke="#b8894a" stroke-width="1.4"/></svg>Garages<br><b>2</b></div>
    </div>
    <h3>New luxury apartment</h3>
    <p>Proin gravida nibh vel velit auctor aliquet aenean</p>
    <div class="actions"><div class="btn-fill">DETAILS</div><span class="book active">BOOK NOW</span></div>
  </article>

  <article class="card">
    <div class="photo" role="img" aria-label="Loft living and dining room with large black framed windows" style="background:linear-gradient(160deg,#f2f2f2,#c8c9cb 55%,#7b7670)"></div>
    <div class="stats">
      <div class="stat"><svg width="22" height="20"><rect x="1" y="1" width="18" height="18" fill="none" stroke="#b8894a" stroke-width="1.4"/><path d="M1 10h9v9" fill="none" stroke="#b8894a" stroke-width="1.4"/></svg>SQFT<br><b>2,016</b></div>
      <div class="stat"><svg width="26" height="20"><path d="M2 18V5M2 12h22v6M5 12V8h8v4" fill="none" stroke="#b8894a" stroke-width="1.4"/></svg>Bedrooms<br><b>3</b></div>
      <div class="stat"><svg width="26" height="20"><path d="M3 10h20c0 5-4 8-10 8S3 15 3 10zM6 10V3h4" fill="none" stroke="#b8894a" stroke-width="1.4"/></svg>Bathrooms<br><b>2</b></div>
      <div class="stat"><svg width="26" height="20"><path d="M2 19V7l11-5 11 5v12M6 19v-8h14v8M6 14h14" fill="none" stroke="#b8894a" stroke-width="1.4"/></svg>Garages<br><b>2</b></div>
    </div>
    <h3>New modern apartment</h3>
    <p>Proin gravida nibh vel velit auctor aliquet aenean</p>
    <div class="actions"><div class="btn-outline">DETAILS</div><span class="book">BOOK NOW</span></div>
  </article>
</div>

<!-- testimonial -->
<div class="abs portrait-frame"></div>
<div class="abs portrait" role="img" aria-label="Portrait of a client in a denim shirt"></div>
<div class="abs quote-mark">“</div>
<section class="abs testimonial">
  <div class="eyebrow">HAPPY CLIENTS</div>
  <h2 class="section-title">Client’s Testimonials</h2>
  <div class="pager">
    <div><svg width="8" height="12"><path d="M6 1L2 6l4 5" stroke="#1c2838" stroke-width="1.5" fill="none"/></svg></div>
    <div class="on"><svg width="8" height="12"><path d="M2 1l4 5-4 5" stroke="#fff" stroke-width="1.5" fill="none"/></svg></div>
  </div>
  <p>Duis sed odio sit amet nibh vulputate cursus a sit amet mauris. Morbi accumsan ipsum velit. Nam nec tellus a odio tincidunt auctor a ornare odio. Sed non mauris vitae erat consequat auctor eu in elit. Class aptent taciti sociosqu ad litora torquent per conubia nostra...</p>
  <div class="author"><i></i><div><strong>Marek Dvořan</strong><span>CEO &amp; President, Northfield Sports</span></div></div>
</section>

<!-- footer -->
<footer class="abs footer">
  <div class="footer-cols">
    <div class="col" style="width:200px">
      <h4>Quick links</h4>
      <ul><li>› Apartments</li><li>› Location</li><li>› Services</li><li>› Gallery</li><li>› News</li></ul>
    </div>
    <div class="col" style="width:200px">
      <h4>Follow us on</h4>
      <ul><li><i class="dot"></i>Friendsbook</li><li><i class="dot"></i>Chirper</li><li><i class="dot"></i>Pinboard</li><li><i class="dot"></i>Snapgram</li><li><i class="dot"></i>Tubecast</li></ul>
    </div>
    <div class="col" style="width:280px">
      <h4>Need to know</h4>
      <ul>
        <li><svg width="12" height="12" viewBox="0 0 24 24" style="flex:none;margin-top:3px"><path fill="#b8894a" d="M6.6 10.8a15 15 0 006.6 6.6l2.2-2.2a1 1 0 011-.25 11.4 11.4 0 003.6.6 1 1 0 011 1V20a1 1 0 01-1 1A17 17 0 013 4a1 1 0 011-1h3.5a1 1 0 011 1c0 1.25.2 2.45.6 3.6a1 1 0 01-.25 1z"/></svg>+420 221 480 391</li>
        <li><svg width="12" height="10" viewBox="0 0 12 10" style="flex:none;margin-top:4px"><rect width="12" height="10" fill="#b8894a"/><path d="M0 0l6 5 6-5" stroke="#131c28" fill="none"/></svg>stay@vltavaresidences.cz</li>
        <li><svg width="12" height="14" viewBox="0 0 12 14" style="flex:none;margin-top:2px"><path fill="#b8894a" d="M6 0a5 5 0 015 5c0 4-5 9-5 9S1 9 1 5a5 5 0 015-5z"/><circle cx="6" cy="5" r="2" fill="#131c28"/></svg><span>Říční nábřeží 18, 110 00 Prague 1,<br>Czech Republic</span></li>
        <li><svg width="12" height="12" viewBox="0 0 12 12" style="flex:none;margin-top:3px"><rect x="1" y="3" width="10" height="8" fill="#b8894a"/><rect x="3" y="0.5" width="6" height="3.5" fill="none" stroke="#b8894a"/></svg>+420 221 480 392</li>
      </ul>
    </div>
    <div class="col" style="flex:1">
      <h4>Our newsletter</h4>
      <p class="news-text">By subscribing to our mailing list you will always be updated with the latest news from us.</p>
      <div class="news-input">Enter email address
        <svg class="abs" style="left:13px;top:17px" width="12" height="10" viewBox="0 0 12 10"><rect width="12" height="10" fill="#b9c1cb"/><path d="M0 0l6 5 6-5" stroke="#fff" fill="none"/></svg>
        <svg class="abs" style="right:14px;top:13px" width="18" height="18" viewBox="0 0 24 24"><path fill="#b8894a" d="M2 21l21-9L2 3v7l15 2-15 2z"/></svg>
      </div>
    </div>
  </div>
  <div class="copyright">© 2017, All Rights Reserved.</div>
</footer>

<div class="abs msg-btn"><div class="ico"><svg width="20" height="18" viewBox="0 0 22 20"><ellipse cx="9" cy="8" rx="8" ry="6.5" fill="#fff"/><path d="M4 13l-2 5 6-3z" fill="#fff"/></svg></div>PLEASE LIVE A MESSAGE</div>
<div class="abs to-top"><svg width="10" height="12"><path d="M5 11V2M1 5l4-4 4 4" stroke="#fff" stroke-width="1.6" fill="none"/></svg></div>

</body>
</html>
```